Medical group practice

We need a flyer design incorporating the three doctors in the practice, there is a general practitioner, ophthalmologist and an obstetrician & Gynaecologist. see the attached file for the concept. will leave the colour design up to you

Target Market(s)

general public

Industry/Entity Type

Health Care

Colors

Designer to choose colors to be used in the design.

Requirements
Must have
• logos included in attachement

```html
<!DOCTYPE html>
<html lang="en">
<head>
<meta charset="utf-8">
<title>Keystone Medical – Flyer</title>
<link rel="stylesheet" href="https://fonts.googleapis.com/css2?family=Oswald:wght@300;500;700&family=Ubuntu:ital,wght@0,400;0,500;0,700;1,400&display=swap">
<style>
:root{
  --red:#d71f2b;
  --blue:#1a73ad;
  --navy:#0f5f93;
  --grey:#8a8a8a;
  --ink:#1f1f1f;
  --panel:#e9e9ea;
  --page:#d8d8d8;
  --white:#ffffff;
}
*{margin:0;padding:0;box-sizing:border-box}
html,body{width:1200px;height:1200px;overflow:hidden;background:var(--page)}
body{font-family:"Ubuntu",sans-serif;color:var(--ink)}
.flyer{position:absolute;left:160px;top:20px;width:880px;height:1160px;background:var(--white);overflow:hidden;box-shadow:0 6px 24px rgba(0,0,0,.18)}
.abs{position:absolute}
.hero-photo{left:410px;top:0;width:470px;height:330px;background:linear-gradient(120deg,#f3ece6 0%,#e9d8c9 30%,#cfe1ee 55%,#eef1ec 75%,#d9c6b6 100%)}
.shape-layer{left:0;top:0;width:880px;height:1160px}
.brand-line{left:40px;top:78px;font-family:"Oswald",sans-serif;font-weight:700;font-size:31px;letter-spacing:.5px}
.brand-line .accent{color:var(--red)}
.brand-line .muted{color:var(--grey);margin-left:10px}
.headline-top{left:44px;top:118px;font-family:"Oswald",sans-serif;font-weight:300;font-size:64px;color:var(--blue);line-height:1}
.headline-mid{left:48px;top:186px;font-family:"Ubuntu",sans-serif;font-size:38px;color:#444;line-height:1}
.headline-rule{left:160px;top:206px;width:220px;height:4px;background:#555}
.headline-big{left:48px;top:208px;font-family:"Oswald",sans-serif;font-weight:700;font-size:92px;color:var(--red);line-height:1.05}
.practice-mark{left:50px;top:420px;display:flex;align-items:center;gap:12px}
.practice-mark .dot{width:34px;height:34px;border-radius:50%;background:var(--red)}
.practice-mark span{font-family:"Ubuntu",sans-serif;font-weight:700;font-size:22px;color:var(--red);line-height:1.1}
.hours{left:215px;top:400px}
.hours h3{color:var(--red);font-weight:500;font-size:19px;margin-bottom:14px}
.hours p{font-size:19px;margin-bottom:6px}
.hours b{color:var(--blue);font-weight:500}
.divider-v{left:490px;top:380px;width:2px;height:150px;background:#777}
.contacts{left:512px;top:372px}
.contacts .role{font-style:italic;color:var(--blue);font-size:19px;margin-top:8px}
.contacts .phone{font-size:19px}
.col{top:640px;width:293px;text-align:center}
.col-1{left:0}.col-2{left:293px}.col-3{left:586px}
.col .mark{height:70px;display:flex;align-items:center;justify-content:center;gap:10px;font-weight:700;font-size:18px}
.col .mark i{width:22px;height:22px;display:inline-block}
.col .doc{color:var(--red);font-weight:500;font-size:20px;margin-top:28px}
.col .cred{color:var(--blue);font-weight:500;font-size:14px}
.col .spec{color:var(--blue);font-style:italic;font-size:19px}
.col .mail{font-size:15px;font-style:italic;font-weight:500;margin-top:4px}
.list{list-style:none;text-align:left;font-size:14px;line-height:1.25}
.list li::before{content:"";display:inline-block;width:7px;height:7px;background:var(--red);transform:rotate(45deg);margin-right:9px;vertical-align:middle}
.list-label{color:var(--blue);font-weight:500;font-size:14px;text-align:left;margin:14px 0 6px}
.col-1 .list{margin:20px 0 0 40px}
.col-2 .list{margin:18px 0 0 30px}
.col-2 .list-label{margin-left:28px}
.subcols{display:flex;gap:18px;margin:14px 0 0 16px}
.subcols .list-label{margin-top:0}
.col-sep{top:800px;width:2px;height:230px;background:#888}
.footer-info{left:0;top:1060px;width:880px;text-align:center;color:var(--white);font-weight:500;font-size:20px;line-height:1.7}
.footer-info svg{vertical-align:-3px;margin-right:8px}
</style>
</head>
<body>
<main class="flyer">
  <div class="abs hero-photo" role="img" aria-label="Photo of a smiling doctor taking a patient's blood pressure in a bright clinic"></div>

  <svg class="abs shape-layer" viewBox="0 0 880 1160" aria-hidden="true">
    <path d="M0 320 Q440 360 880 290 L880 350 L0 350Z" fill="var(--white)"/>
    <path d="M0 330 Q440 372 880 300" fill="none" stroke="var(--blue)" stroke-width="7"/>
    <path d="M0 610 Q420 500 880 560 L880 1160 L0 1160Z" fill="var(--panel)"/>
    <path d="M0 610 Q420 500 880 560" fill="none" stroke="var(--blue)" stroke-width="8"/>
    <path d="M0 1060 Q440 990 880 1010 L880 1160 L0 1160Z" fill="var(--red)"/>
    <path d="M0 1072 Q440 1004 880 1024 L880 1160 L0 1160Z" fill="var(--white)"/>
    <path d="M0 1080 Q440 1012 880 1032 L880 1160 L0 1160Z" fill="var(--blue)"/>
  </svg>

  <div class="abs brand-line"><span class="accent">KEYSTONE</span><span class="muted">MEDICAL</span></div>
  <div class="abs headline-top">YOUR HEALTH</div>
  <div class="abs headline-mid">is our</div>
  <div class="abs headline-rule"></div>
  <div class="abs headline-big">PRIORITY</div>

  <div class="abs practice-mark"><div class="dot"></div><span>Keystone<br>Medical</span></div>

  <section class="abs hours">
    <h3>OPENING HOURS :</h3>
    <p><b>Monday:</b> Fridays : 9am-6pm,</p>
    <p><b>Saturdays :</b> 10am – 5pm</p>
  </section>

  <div class="abs divider-v"></div>

  <section class="abs contacts">
    <div class="role">General Practitioner</div>
    <div class="phone">(555) 210 4471</div>
    <div class="role">Ophthalmologist</div>
    <div class="phone">(555) 210 4482</div>
    <div class="role">Obstetrician/Gynaecologist</div>
    <div class="phone">(555) 210 4493 / (555) 318 7720</div>
  </section>

  <section class="abs col col-1">
    <div class="mark" style="color:var(--blue)"><i style="background:var(--blue)"></i>Ellery Family Care</div>
    <div class="doc">Dr. Marcus Ellery, MD.</div>
    <div class="spec">General Practitioner</div>
    <div class="mail">m.ellery.doc@example.com</div>
    <ul class="list">
      <li>General Checks</li>
      <li>Annual Check ups</li>
      <li>Wound Care/Dressings</li>
      <li>Incision &amp; Drainage</li>
      <li>Suturing lacerations</li>
      <li>Pain Injections</li>
      <li>Glucose checks</li>
      <li>Foreign Body Removal</li>
    </ul>
  </section>

  <section class="abs col col-2">
    <div class="mark" style="color:#6a2a7a"><i style="background:#6a2a7a;border-radius:50%"></i>Clearview Eye Services</div>
    <div class="doc">Dr. Lucia R. Ferrand</div>
    <div class="spec">MD. Surgeon Ophthalmologist</div>
    <div class="mail">lucia.eyes@example.com</div>
    <ul class="list">
      <li>Eyes disease examination</li>
      <li>Surgery of Pterygium</li>
      <li>Cataract</li>
      <li>Glaucoma</li>
    </ul>
    <div class="list-label">EMERGENCY:</div>
    <ul class="list">
      <li>Conjunctivitis</li>
      <li>Traumatism</li>
      <li>Foreign body<br>&nbsp;&nbsp;&nbsp;&nbsp;and more...</li>
    </ul>
  </section>

  <section class="abs col col-3">
    <div class="mark" style="color:var(--navy)"><i style="background:#2e9a4a;border-radius:50%"></i>Dalvi Women's Care</div>
    <div class="doc" style="margin-top:18px">Dr. Kiran Dalvi</div>
    <div class="cred">BMedSci, MBBS, DM (O&amp;G), FACOG</div>
    <div class="spec">Obstetrician &amp; Gynaecologist</div>
    <div class="mail">drdalvi@example.com</div>
    <div class="subcols">
      <div>
        <div class="list-label">OBSTETRICS:</div>
        <ul class="list">
          <li>Prenatal Care</li>
          <li>Delivery</li>
          <li>Postnatal checks</li>
          <li>High Risk<br>&nbsp;&nbsp;&nbsp;&nbsp;pregnancy</li>
        </ul>
      </div>
      <div>
        <div class="list-label">GYNAECOLOGY :</div>
        <ul class="list">
          <li>Pap smears,</li>
          <li>Abnormal vaginal</li>
          <li>bleeding,</li>
          <li>Fibroids,</li>
          <li>Colposcopy,</li>
          <li>Family planning,</li>
          <li>Infertility,</li>
          <li>Cancer screening,</li>
          <li style="list-style:none">And More....</li>
        </ul>
      </div>
    </div>
  </section>

  <div class="abs col-sep" style="left:292px"></div>
  <div class="abs col-sep" style="left:585px"></div>

  <div class="abs footer-info">
    <div><svg width="18" height="18" viewBox="0 0 24 24"><path fill="#fff" d="M6.6 10.8a15 15 0 0 0 6.6 6.6l2.2-2.2a1 1 0 0 1 1-.25 11.4 11.4 0 0 0 3.6.57 1 1 0 0 1 1 1V20a1 1 0 0 1-1 1A17 17 0 0 1 3 4a1 1 0 0 1 1-1h3.5a1 1 0 0 1 1 1c0 1.25.2 2.45.57 3.57a1 1 0 0 1-.25 1z"/></svg>(555) 240 1100 / 1101</div>
    <div><svg width="16" height="20" viewBox="0 0 16 20"><path fill="none" stroke="#fff" stroke-width="2" d="M8 19s6-6.5 6-11A6 6 0 0 0 2 8c0 4.5 6 11 6 11z"/><circle cx="8" cy="8" r="2" fill="#fff"/></svg>42 Harbour Road, Port Leland, Westbay</div>
  </div>
</main>
</body>
</html>
```